BHSM Business Card Design Project

We are a Wedding Film company in Charleston, SC In need of a unique business card. Our website is www.brightharborstudiomedia.com. Check us out to get an idea of who we are and what we do. The design should be upscale but not pretentious. Modern but not cheesy. I will most likely have our cards printed by Zell on the Plume design. I'm also liking the raised designs for our logo. The Wedding Films in our logo on our site is blue so feel free to manipulate our logo for your designs as well.

Industry/Entity Type

Business

Requirements
Must have
• This is the info I want on the card:

Derek Halloway
Storyteller

Brightharbor Studio Media
www.brightharborstudiomedia.com

843.627.4150
derek@brightharborstudiomedia.com

```html
<!DOCTYPE html>
<html lang="en">
<head>
<meta charset="utf-8">
<title>Brightharbor Studio Media – Business Card</title>
<link href="https://fonts.googleapis.com/css2?family=Quicksand:wght@400;500;600&display=swap" rel="stylesheet">
<style>
  :root {
    --backdrop: #e6eaed;
    --card: #ffffff;
    --stripe: #f1f4f7;
    --gold: #a88b57;
    --blue: #3a8ed6;
    --blue-pale: #c9def0;
    --ink: #2f2f2f;
    --rule: #b9b9b9;
  }
  * { box-sizing: border-box; margin: 0; padding: 0; }
  html, body { width: 1200px; height: 960px; overflow: hidden; }
  body {
    background: var(--backdrop);
    font-family: "Quicksand", sans-serif;
    position: relative;
  }
  .card {
    position: absolute;
    left: 250px;
    width: 700px;
    height: 400px;
    background: var(--card);
    box-shadow: 0 6px 18px rgba(0,0,0,0.12);
    overflow: hidden;
  }
  /* Front */
  .card-front {
    top: 60px;
    background: repeating-linear-gradient(90deg, var(--card) 0 22px, var(--stripe) 22px 44px);
  }
  .ornament {
    position: absolute;
    background: radial-gradient(circle at center, var(--blue-pale) 0%, rgba(201,222,240,0.35) 70%, rgba(201,222,240,0) 100%);
  }
  .ornament-top-right { top: -20px; right: -20px; width: 170px; height: 210px; border-radius: 0 0 0 60%; }
  .ornament-bottom-left { bottom: -20px; left: -20px; width: 180px; height: 260px; border-radius: 0 60% 0 0; }
  .brand {
    position: absolute;
    top: 0; left: 0; right: 0; bottom: 0;
    display: flex;
    flex-direction: column;
    align-items: center;
    justify-content: center;
    gap: 26px;
  }
  .brand-mark {
    width: 120px; height: 120px;
    border-radius: 50%;
    background: var(--gold);
  }
  .brand-name {
    font-size: 44px;
    font-weight: 500;
    color: var(--gold);
    letter-spacing: 0.5px;
  }
  /* Back */
  .card-back { top: 500px; }
  .contact {
    position: absolute;
    left: 44px;
    top: 58px;
    width: 340px;
  }
  .person-name { font-size: 26px; font-weight: 500; color: var(--gold); letter-spacing: 0.5px; }
  .person-title { font-size: 19px; font-weight: 500; color: var(--ink); margin-top: 10px; }
  .divider { border-top: 2px dotted var(--rule); width: 280px; margin: 14px 0; }
  .contact-line { font-size: 15px; font-weight: 500; color: var(--ink); line-height: 1.7; white-space: nowrap; }
  .contact-line .label { color: var(--blue); margin-right: 4px; }
  .company { font-size: 16px; font-weight: 500; color: var(--ink); line-height: 1.6; }
  .website { font-size: 16px; font-weight: 600; color: var(--blue); white-space: nowrap; }
  .tree-art {
    position: absolute;
    right: 0; top: 40px;
    width: 250px; height: 360px;
    background: linear-gradient(160deg, #5aa4e0 0%, var(--blue) 60%, #2f7fc4 100%);
    border-radius: 48% 0 0 0 / 35% 0 0 0;
  }
</style>
</head>
<body>
  <section class="card card-front" aria-label="Card front">
    <div class="ornament ornament-top-right" role="img" aria-label="Pale blue swirl ornament"></div>
    <div class="ornament ornament-bottom-left" role="img" aria-label="Pale blue swirl ornament"></div>
    <div class="brand">
      <div class="brand-mark"></div>
      <div class="brand-name">Brightharbor Studio Media</div>
    </div>
  </section>

  <section class="card card-back" aria-label="Card back">
    <div class="contact">
      <div class="person-name">Derek Halloway</div>
      <div class="person-title">Storyteller</div>
      <div class="divider"></div>
      <div class="contact-line"><span class="label">t:</span>843.627.4150</div>
      <div class="contact-line"><span class="label">e:</span>derek@brightharborstudiomedia.com</div>
      <div class="divider"></div>
      <div class="company">Brightharbor Studio Media</div>
      <div class="website">www.brightharborstudiomedia.com</div>
    </div>
    <div class="tree-art" role="img" aria-label="Blue leafy tree illustration with film reel at its roots"></div>
  </section>
</body>
</html>
```